Stationery Design Project

We need a Stationery Design for automotive industry.
Updates

Target Market(s)

Mechanic garage and Mechanics

Industry/Entity Type

Automotive

Requirements
Must have
• The logo company and the legal information.

We are a car spart parts and tools delar
Nice to have
• We like something elegant and simple.
Should not have

```html
<!DOCTYPE html>
<html lang="en">
<head>
<meta charset="utf-8">
<title>Northgate Auto Supply – Stationery</title>
<link rel="stylesheet" href="https://fonts.googleapis.com/css2?family=Arimo:wght@400;700&display=swap">
<style>
  :root {
    --ink: #231f20;
    --paper: #ffffff;
    --accent: #5a63b3;
    --text: #4a4a4a;
    --backdrop: #d9d9d9;
  }
  * { margin: 0; padding: 0; box-sizing: border-box; }
  html, body { width: 1200px; height: 849px; overflow: hidden; }
  body {
    position: relative;
    background: var(--backdrop);
    font-family: "Arimo", Arial, sans-serif;
    color: var(--text);
  }
  .sheet {
    position: absolute;
    background: var(--paper);
    overflow: hidden;
  }
  .stripe {
    position: absolute;
    top: 0; bottom: 0;
    z-index: 1;
    background: var(--ink);
    box-shadow: 0 0 0 2px var(--paper), 0 0 0 3px var(--ink);
  }
  .brand {
    position: absolute;
    z-index: 2;
    display: flex;
    align-items: center;
    justify-content: center;
    background: var(--ink);
    color: var(--paper);
    font-weight: 700;
    letter-spacing: 1px;
    white-space: nowrap;
  }
  .brand--plain { position: static; background: none; gap: 8px; }
  .brand-dot {
    width: 12px; height: 12px;
    border-radius: 50%;
    background: var(--paper);
    flex: none;
  }

  .footer {
    position: absolute;
    display: flex;
    font-size: 8px;
    line-height: 11px;
    color: var(--text);
    white-space: nowrap;
  }
  .footer > div:nth-child(1) { width: 136px; }
  .footer > div:nth-child(2) { width: 82px; }
  .footer > div:nth-child(3) { width: 94px; }
  .footer .label, .footer .company { color: var(--accent); font-weight: 700; }

  /* Letterhead */
  .letterhead { left: 28px; top: 40px; width: 594px; height: 770px; }
  .letterhead .stripe { left: 62px; width: 88px; }
  .letterhead .brand { left: 9px; top: 35px; width: 195px; height: 65px; font-size: 17px; }
  .letterhead .footer { left: 162px; top: 729px; }

  /* Business card front */
  .card-front { left: 585px; top: 98px; width: 244px; height: 140px; }
  .card-front .stripe { left: 15px; width: 78px; }
  .card-front .brand { left: 5px; top: 17px; width: 96px; height: 43px; font-size: 9px; letter-spacing: 0.5px; }
  .card-front .holder { position: absolute; right: 12px; top: 10px; text-align: right; }
  .card-front .holder-name { font-size: 10px; font-weight: 700; color: var(--ink); }
  .card-front .holder-role { font-size: 8px; color: var(--accent); }
  .card-front .contact {
    position: absolute; right: 12px; top: 84px; text-align: right;
    font-size: 6.5px; line-height: 8.5px;
  }
  .card-front .contact .label { color: var(--accent); font-weight: 700; }

  /* Business card back */
  .card-back {
    left: 862px; top: 98px; width: 243px; height: 140px;
    background: var(--ink);
    display: flex; align-items: center; justify-content: center;
  }
  .card-back .brand { font-size: 15px; }

  /* Envelope */
  .envelope { left: 509px; top: 270px; width: 596px; height: 406px; }
  .envelope-flap {
    position: absolute; left: 0; top: 0; width: 596px; height: 116px;
    background: var(--ink);
    border-top-left-radius: 34px 14px;
    display: flex; align-items: center; justify-content: center;
  }
  .envelope-flap .brand { font-size: 15px; transform: rotate(180deg); }
  .envelope .stripe { left: 63px; width: 88px; top: 116px; }
  .envelope .brand--front { left: 11px; top: 145px; width: 196px; height: 70px; font-size: 16px; }
  .envelope .footer { left: 174px; top: 371px; }
</style>
</head>
<body>

  <section class="sheet letterhead" aria-label="Letterhead">
    <div class="stripe"></div>
    <div class="brand">NORTHGATE</div>
    <div class="footer">
      <div><span class="company">Northgate Auto Supply Pty Ltd.</span><br>ABN&nbsp; 41 902 337 518</div>
      <div>P.O. Box 000<br>Sydney NSW 0000</div>
      <div><span class="label">Phone</span> (02) 0000 0000<br><span class="label">Fax</span>&nbsp;&nbsp;&nbsp;&nbsp;&nbsp;&nbsp; (02) 0000 0000</div>
      <div>info@northgateauto.com.au<br>www.northgateauto.com.au</div>
    </div>
  </section>

  <section class="sheet card-front" aria-label="Business card front">
    <div class="stripe"></div>
    <div class="brand">NORTHGATE</div>
    <div class="holder">
      <div class="holder-name">Alex Carter</div>
      <div class="holder-role">Director</div>
    </div>
    <div class="contact">
      P.O. Box 000<br>
      Sydney NSW 0000<br>
      <span class="label">Phone</span>&nbsp; (02) 0000 0000<br>
      <span class="label">Fax</span>&nbsp;&nbsp;&nbsp;&nbsp;&nbsp; (02) 0000 0000<br>
      info@northgateauto.com.au<br>
      www.northgateauto.com.au
    </div>
  </section>

  <section class="sheet card-back" aria-label="Business card back">
    <div class="brand brand--plain"><span class="brand-dot"></span><span>NORTHGATE</span></div>
  </section>

  <section class="sheet envelope" aria-label="Envelope">
    <div class="envelope-flap">
      <div class="brand brand--plain"><span class="brand-dot"></span><span>NORTHGATE</span></div>
    </div>
    <div class="stripe"></div>
    <div class="brand brand--front">NORTHGATE</div>
    <div class="footer">
      <div><span class="company">Northgate Auto Supply Pty Ltd.</span><br>ABN&nbsp; 41 902 337 518</div>
      <div>P.O. Box 000<br>Sydney NSW 0000</div>
      <div><span class="label">Phone</span> (02) 0000 0000<br><span class="label">Fax</span>&nbsp;&nbsp;&nbsp;&nbsp;&nbsp;&nbsp; (02) 0000 0000</div>
      <div>info@northgateauto.com.au<br>www.northgateauto.com.au</div>
    </div>
  </section>

</body>
</html>
```